Business Card Design

Lintel PR is a public relations consultancy service for the self build, home refurbishment and home improvement market.
It represents everything about 'home' so envisage logo featuring maybe roof pitch over the 'A' of Lintel. Colour/font undecided.

Industry/Entity Type

Home Improvement

Contact Information for Business Card

Fenella Stroudwick
fenella@lintelpr-example.co.uk
Telephone Direct: 0700 555 0142

```html
<!DOCTYPE html>
<html lang="en">
<head>
<meta charset="utf-8">
<title>Lintel PR Business Card</title>
<link href="https://fonts.googleapis.com/css2?family=Bodoni+Moda:wght@700&display=swap" rel="stylesheet">
<style>
  :root {
    --backdrop: #ecebe8;
    --card: #ffffff;
    --ink: #161616;
    --band: #1c1b1b;
    --band-text: #ffffff;
    --brand-green: #8cc63f;
    --brand-blue: #1b6cc0;
    --divider: #b8c4cc;
  }
  * { box-sizing: border-box; margin: 0; padding: 0; }
  html, body {
    width: 1200px;
    height: 905px;
    overflow: hidden;
    background: var(--backdrop);
    font-family: "Bodoni Moda", "Didot", serif;
  }
  .business-card {
    position: absolute;
    left: 150px;
    top: 155px;
    width: 900px;
    height: 595px;
    background: var(--card);
    box-shadow: 0 12px 30px rgba(0, 0, 0, 0.18);
  }
  .brand-lockup {
    position: absolute;
    left: 0;
    right: 0;
    top: 190px;
    display: flex;
    justify-content: center;
    align-items: center;
    gap: 16px;
  }
  .brand-mark-square {
    width: 30px;
    height: 30px;
    background: var(--brand-green);
  }
  .brand-name {
    font-size: 58px;
    font-weight: 700;
    letter-spacing: 3px;
    color: var(--ink);
    line-height: 1;
  }
  .contact-row {
    position: absolute;
    left: 0;
    right: 0;
    top: 330px;
    height: 105px;
  }
  .holder-name {
    position: absolute;
    left: 48px;
    top: 32px;
    font-size: 36px;
    font-weight: 700;
    color: var(--ink);
  }
  .row-divider {
    position: absolute;
    left: 450px;
    top: 0;
    width: 2px;
    height: 105px;
    background: linear-gradient(to bottom, transparent, var(--divider) 30%, var(--divider) 70%, transparent);
  }
  .phone-line {
    position: absolute;
    left: 520px;
    top: 28px;
    display: flex;
    align-items: center;
    gap: 6px;
    font-size: 38px;
    font-weight: 700;
    color: var(--ink);
  }
  .phone-icon { width: 34px; height: 34px; }
  .email-band {
    position: absolute;
    left: 0;
    right: 0;
    top: 497px;
    height: 44px;
    background: var(--band);
    display: flex;
    align-items: center;
    padding-left: 230px;
    gap: 10px;
  }
  .email-icon { width: 26px; height: 20px; }
  .email-address {
    font-size: 28px;
    font-weight: 700;
    color: var(--band-text);
    line-height: 1;
  }
</style>
</head>
<body>
  <div class="business-card">
    <div class="brand-lockup">
      <span class="brand-mark-square"></span>
      <span class="brand-name">LINTEL PR</span>
    </div>

    <div class="contact-row">
      <div class="holder-name">Fenella Stroudwick</div>
      <div class="row-divider"></div>
      <div class="phone-line">
        <svg class="phone-icon" viewBox="0 0 24 24" aria-hidden="true">
          <path fill="var(--brand-green)" d="M6.6 2.5c.6-.4 1.4-.3 1.8.3l2.2 3.2c.4.6.3 1.4-.2 1.9L9 9.2c1 2.3 3.4 4.9 5.8 5.9l1.3-1.4c.5-.5 1.3-.6 1.9-.2l3.2 2.2c.6.4.7 1.2.3 1.8l-1.6 2.4c-.5.7-1.4 1.1-2.3.9C9.8 19.4 4.6 14.2 3.2 6.4c-.2-.9.2-1.8.9-2.3z"/>
        </svg>
        <span>0700 555 0142</span>
      </div>
    </div>

    <div class="email-band">
      <svg class="email-icon" viewBox="0 0 26 20" aria-hidden="true">
        <rect x="1" y="1" width="24" height="18" fill="none" stroke="var(--band-text)" stroke-width="1.8"/>
        <path d="M1 1l12 10L25 1M1 19l9-8M25 19l-9-8" fill="none" stroke="var(--band-text)" stroke-width="1.5"/>
      </svg>
      <span class="email-address">fenella@lintelpr-example.co.uk</span>
    </div>
  </div>
</body>
</html>
```